Hole-in-the-wall Food Kiosk Flyer

We would like to outsource a flyer design.

CLIENT: Parolcito Lechon + Wraps
DESCRIPTION: Food Take-out and Delivery

PROJECT GOAL:
- To be able to make a flyer that showcases the company intro and its menu.
- The purpose of this flyer is for customers to be able to keep it and take it out whenever they feel the need to order some food.

------------------------------------------------------------------------------------
CLIENT DESCRIPTION:

Parolcito is a hole-in-the-wall food kiosk specializing in Mexican-inspired Filipino food.

Our menu booasts a delectable range of Filipino favorites such as sisig and rice meals meshed with some well-loved Mexican flair. Crispy Sisig in Toasted Tacos, anyone?

We pride ourselves in serving familiar, close-to-home savor with a minor twist. So if you're hungry for comfort food, but can't quite put your finger on what, come to Parolcito for food that hits the spot.

BRAND IMAGE:
- Fun, Non-intimidating, Rustic, Homey

https://www.snapgallerio.com/parolcito_lechonwraps/

FOOD MENU:

A. SISIG
- Crispy Sisig
- Chicken Adobo Sisig
* Can be served as: 1) Rice Meal 2) Taco 3) Burrito 4) For Sharing of 2-3 persons.
* Prices are different for each format (If it's a rice meal, taco, etc.)

B. CRISPY SINIGANG
- rice meal
- for sharing

C. BEEF STEAK
- burrito
- taco

D. CRISPY CHICKEN WINGS
- rice meal
- for sharing

E. ULTIMATE NACHOS

F. BLACK TAPA
- rice meal served with egg

G. BEEF BURGER
- as a rice meal served with egg
- or served in a bun.

H. DRINKS
- Vento Iced Tea
- Bottled Water

We included some photos and the logo to give you inspiration.

Thanks!

Target Market(s)

- Young Adults, aged 18-32, working/residing in Rockwell Area, Makati City Philippines.
- They are open to new ideas/willing to try new things.
- They are a bit budget conscious. They want delicious, home-feel food.
- They are avid social media subscribers. They are mostly online.

Industry/Entity Type

Food Store

Colors
f37122
9bcb3b
ffc214

Requirements
Must have
• THINGS TO THINK ABOUT:
• - Final size should be 3.85"x8.85". This can be a folded size or a spread out size. The idea is for it to fit most mailboxes with ease.
• - Contact info must include, celphone, facebook, and instagram.
• - Flyer has to be appetizing and appealing. Make use of food photos.
Nice to have
• - The flyer should be useful in some other manner rather than just being a menu flyer. (Maybe it can also be a ruler, etc.)
• - Colors can be up to you.

```html
<!DOCTYPE html>
<html lang="en">
<head>
<meta charset="utf-8">
<title>Parolcito Lechon + Wraps – Contact Panel</title>
<link href="https://fonts.googleapis.com/css2?family=Varela+Round&display=swap" rel="stylesheet">
<style>
  :root {
    --plank-sky: #cfe6f3;
    --plank-coral: #f28466;
    --plank-coral-deep: #ef7a5a;
    --plank-mist: #e2ecee;
    --plank-blue: #b9dcef;
    --plank-blue-deep: #8ecbee;
    --plank-teal: #5ccab7;
    --plank-pale: #e3eaea;
    --grain-light: rgba(255, 255, 255, 0.32);
    --grain-dark: rgba(0, 0, 0, 0.035);
    --ink: #161616;
  }
  * { margin: 0; padding: 0; box-sizing: border-box; }
  html, body { width: 1200px; height: 2757px; overflow: hidden; }
  body { font-family: "Varela Round", "Helvetica Neue", Arial, sans-serif; color: var(--ink); background: var(--plank-mist); }

  .flyer-panel { position: relative; width: 1200px; height: 2757px; overflow: hidden; }

  .plank { position: absolute; left: 0; width: 1200px; }
  .plank::after {
    content: "";
    position: absolute;
    inset: 0;
    background:
      repeating-linear-gradient(180deg, transparent 0 17px, var(--grain-light) 17px 20px, transparent 20px 41px, var(--grain-dark) 41px 43px, transparent 43px 64px),
      repeating-linear-gradient(90deg, transparent 0 130px, rgba(255, 255, 255, 0.08) 130px 210px, transparent 210px 330px);
  }
  .plank--sky        { top: 0;      height: 114px; background: linear-gradient(90deg, var(--plank-sky), #bfe0f3 55%, #d6eaf3); }
  .plank--coral-top  { top: 114px;  height: 410px; background: linear-gradient(180deg, #f38d6f, var(--plank-coral) 50%, var(--plank-coral-deep)); }
  .plank--mist       { top: 524px;  height: 376px; background: linear-gradient(90deg, var(--plank-mist), #edf1ef 50%, #d8e9f2); }
  .plank--blue       { top: 900px;  height: 396px; background: linear-gradient(90deg, #c9e4f1, var(--plank-blue) 55%, var(--plank-blue-deep)); }
  .plank--coral-mid  { top: 1296px; height: 399px; background: linear-gradient(180deg, #f38b6b, var(--plank-coral)); }
  .plank--teal       { top: 1695px; height: 410px; background: var(--plank-teal); }
  .plank--pale       { top: 2105px; height: 386px; background: linear-gradient(90deg, var(--plank-pale), #eef1ef 50%, #dae6ea); }
  .plank--coral-bottom { top: 2491px; height: 266px; background: var(--plank-coral); }

  .brand__name {
    position: absolute;
    top: 690px;
    left: 0;
    width: 1200px;
    text-align: center;
    font-size: 176px;
    line-height: 1;
    letter-spacing: 4px;
  }
  .brand__tagline {
    position: absolute;
    top: 836px;
    right: 217px;
    font-size: 31px;
    line-height: 1;
  }

  .contact-phone {
    position: absolute;
    top: 1050px;
    left: 0;
    width: 1200px;
    text-align: center;
    font-size: 80px;
    line-height: 1;
    letter-spacing: 3px;
  }
  .contact-address {
    position: absolute;
    top: 1448px;
    left: 0;
    width: 1200px;
    text-align: center;
    font-style: normal;
    font-size: 47px;
    line-height: 64px;
  }

  .social { position: absolute; display: flex; align-items: center; gap: 24px; font-size: 52px; line-height: 1; }
  .social__mark { width: 97px; height: 97px; background: var(--ink); border-radius: 6px; flex: none; }
  .social--facebook  { top: 1862px; left: 423px; }
  .social--instagram { top: 2246px; left: 276px; }
</style>
</head>
<body>
  <main class="flyer-panel">
    <div class="plank plank--sky"></div>
    <div class="plank plank--coral-top"></div>
    <div class="plank plank--mist"></div>
    <div class="plank plank--blue"></div>
    <div class="plank plank--coral-mid"></div>
    <div class="plank plank--teal"></div>
    <div class="plank plank--pale"></div>
    <div class="plank plank--coral-bottom"></div>

    <header class="brand">
      <div class="brand__name">Parolcito</div>
      <div class="brand__tagline">lechon + wrap shop</div>
    </header>

    <p class="contact-phone">+63 917 240 6618</p>

    <address class="contact-address">
      41 B Malvar St. Corner Orion St.<br>
      Makati, Philippines
    </address>

    <div class="social social--facebook">
      <span class="social__mark"></span>
      <span class="social__handle">Parolcito</span>
    </div>

    <div class="social social--instagram">
      <span class="social__mark"></span>
      <span class="social__handle">parolcito_lechonwraps</span>
    </div>
  </main>
</body>
</html>
```